Q7 Labs

I need a business card for my software development company. I have the logo already and will provide that to you. We create web and mobile applications for businesses. I want it to be an edgy design and am thinking (but not required), just the logo on one side and the contact info on the other.

I will upload your finished file to either PrintHarbor or Zib for printing.

Target Market(s)

Business owners who will appreciate an edgy and modern culture in the consultant they hire.

Industry/Entity Type

Software

Requirements
Must have
• Contact info...

Dale Fenwick
President
Dale@q7labs-example.co
http://q7labs-example.co
555.013.4927
@dalefwk
Nice to have
• The address is optional. It's...

2214 Marlow Court
Harborview, VA 23999

Also optional are icons next to the email, twitter, phone and URL to clarify what they are (ex: a twitter icon next to @dalefwk)

```html
<!DOCTYPE html>
<html lang="en">
<head>
<meta charset="utf-8">
<title>Q7 Labs Business Card</title>
<link rel="stylesheet" href="https://fonts.googleapis.com/css2?family=Oswald:wght@500;600&family=Questrial&display=swap">
<style>
  :root {
    --navy: #2b2a4e;
    --orange: #c8602a;
    --white: #ffffff;
    --paper: #f7f7f7;
    --stage: #e6e6e8;
    --grey: #8a8a8a;
  }
  * { box-sizing: border-box; margin: 0; padding: 0; }
  html, body { width: 1200px; height: 1000px; overflow: hidden; }
  body {
    background: var(--stage);
    font-family: "Questrial", "Century Gothic", sans-serif;
    display: flex;
    flex-direction: column;
    align-items: center;
    justify-content: center;
    gap: 60px;
  }
  .card {
    position: relative;
    width: 700px;
    height: 400px;
    overflow: hidden;
    box-shadow: 0 10px 28px rgba(0,0,0,0.15);
  }

  /* Front */
  .card-front { background: var(--navy); }
  .card-front .brand {
    position: absolute;
    left: 50px;
    top: 120px;
    display: flex;
    align-items: center;
    gap: 14px;
    font-family: "Oswald", sans-serif;
    font-weight: 600;
    font-size: 64px;
    color: var(--white);
    line-height: 1;
  }
  .brand-mark { width: 16px; height: 16px; background: var(--orange); }
  .card-front .url-band {
    position: absolute;
    left: 330px;
    right: 0;
    top: 60px;
    height: 50px;
    background: var(--orange);
    display: flex;
    align-items: center;
    padding-left: 52px;
    color: var(--white);
    font-size: 15px;
    letter-spacing: 2px;
  }

  /* Back */
  .card-back { background: var(--paper); color: var(--navy); }
  .card-back .brand {
    position: absolute;
    right: 50px;
    top: 46px;
    display: flex;
    align-items: center;
    gap: 12px;
    font-family: "Oswald", sans-serif;
    font-weight: 600;
    font-size: 56px;
    color: var(--navy);
    line-height: 1;
  }
  .card-back .brand-mark { background: var(--grey); width: 14px; height: 14px; }
  .name-band {
    position: absolute;
    left: 0;
    top: 150px;
    width: 400px;
    height: 50px;
    background: var(--orange);
    display: flex;
    align-items: center;
    padding-left: 34px;
    gap: 10px;
    font-family: "Oswald", sans-serif;
    color: var(--white);
  }
  .name-band .name { font-size: 28px; font-weight: 500; }
  .name-band .dot { width: 7px; height: 7px; background: var(--white); }
  .name-band .role { font-size: 18px; font-weight: 600; letter-spacing: 0.5px; }
  .address {
    position: absolute;
    right: 50px;
    top: 164px;
    text-align: right;
    font-size: 16px;
    line-height: 1.55;
  }
  .contact-list {
    position: absolute;
    left: 60px;
    bottom: 56px;
    list-style: none;
    font-size: 17px;
    line-height: 1;
  }
  .contact-list li { display: flex; align-items: center; gap: 18px; margin-top: 14px; }
  .contact-list svg { width: 16px; height: 16px; fill: var(--orange); flex: none; }
</style>
</head>
<body>

  <section class="card card-front" aria-label="Card front">
    <div class="brand"><span class="brand-mark"></span>Q7 Labs</div>
    <div class="url-band">www.q7labs-example.co</div>
  </section>

  <section class="card card-back" aria-label="Card back">
    <div class="brand"><span class="brand-mark"></span>Q7 Labs</div>
    <div class="name-band">
      <span class="name">Dale Fenwick</span>
      <span class="dot"></span>
      <span class="role">PRESIDENT</span>
    </div>
    <p class="address">2214 Marlow Court<br>Harborview, VA 23999</p>
    <ul class="contact-list">
      <li>
        <svg viewBox="0 0 16 16" aria-hidden="true"><path d="M3.5 1 6 1.5 7 5 5.3 6.3a8.5 8.5 0 0 0 4.4 4.4L11 9l3.5 1 .5 2.5-2 2C6.5 14.5 1.5 9.5 1.5 3z"/></svg>
        555.013.4927
      </li>
      <li>
        <svg viewBox="0 0 16 16" aria-hidden="true"><path d="M1 3h14v10H1z M2.5 4.5 8 9l5.5-4.5" fill="none" stroke="var(--orange)" stroke-width="1.8"/></svg>
        Dale@q7labs-example.co
      </li>
      <li>
        <svg viewBox="0 0 16 16" aria-hidden="true"><circle cx="8" cy="8" r="6.5"/></svg>
        @dalefwk
      </li>
    </ul>
  </section>

</body>
</html>
```